Business Card Design

I give lessons and clinics for dressage riders
I would like the design to be an outline (with broad lines) of a dressage horse and rider with in background of whole card with print over top tan or parchment card with burgundy print

Industry/Entity Type

Business

Contact Information for Business Card

Tod Harlick
555-317-0492
Classical dressage training for the modern American
Clinics, lessons, training level -Prix St. George

Requirements
Must have
• broad lined outline of dressage horse and rider

```html
<!DOCTYPE html>
<html lang="en">
<head>
<meta charset="utf-8">
<title>Tod Harlick — Classical Dressage Training</title>
<link rel="stylesheet" href="https://fonts.googleapis.com/css2?family=Jost:ital,wght@1,400;1,500&display=swap">
<style>
  :root {
    --burgundy: #c8000a;
    --aqua: #33e6ee;
    --paper: #ffffff;
  }
  html, body {
    margin: 0;
    padding: 0;
    width: 1200px;
    height: 702px;
    overflow: hidden;
    background: var(--paper);
  }
  .card {
    position: relative;
    width: 1200px;
    height: 702px;
    background: var(--paper);
    font-family: "Jost", "Futura", sans-serif;
    font-style: italic;
    color: var(--burgundy);
  }
  .frame-outer {
    position: absolute;
    left: 22px; top: 20px;
    width: 1150px; height: 654px;
    border: 4.5px solid var(--burgundy);
    box-sizing: border-box;
  }
  .frame-inner {
    position: absolute;
    left: 44px; top: 44px;
    width: 1110px; height: 612px;
    border: 4px solid var(--aqua);
    box-sizing: border-box;
  }
  .horizon-rule {
    position: absolute;
    left: 102px; top: 211px;
    width: 1001px; height: 10px;
    background: var(--burgundy);
  }
  .rider-figure {
    position: absolute;
    left: 70px; top: 100px;
    width: 600px; height: 410px;
  }
  .name {
    position: absolute;
    left: 886px; top: 296px;
    transform: translateX(-50%);
    margin: 0;
    font-size: 75px;
    font-weight: 400;
    line-height: 1;
    white-space: nowrap;
  }
  .phone {
    position: absolute;
    left: 886px; top: 376px;
    transform: translateX(-50%);
    margin: 0;
    font-size: 32px;
    letter-spacing: 1px;
    line-height: 1;
    white-space: nowrap;
  }
  .services {
    position: absolute;
    left: 363px; top: 518px;
    transform: translateX(-50%);
    margin: 0;
    text-align: center;
    white-space: nowrap;
    line-height: 1;
  }
  .services .line { display: block; font-size: 26.5px; }
  .services .line + .line { margin-top: 3px; }
  .services .level { font-size: 31.5px; margin-top: 9px; font-weight: 500; }
</style>
</head>
<body>
  <main class="card">
    <div class="frame-outer"></div>
    <div class="frame-inner"></div>
    <div class="horizon-rule"></div>

    <svg class="rider-figure" viewBox="0 0 600 410" role="img" aria-label="Silhouette of a dressage horse and rider in motion, in burgundy">
      <defs>
        <radialGradient id="figureTone" cx="50%" cy="50%" r="50%">
          <stop offset="0%" stop-color="#c8000a" stop-opacity="0.9"/>
          <stop offset="60%" stop-color="#c8000a" stop-opacity="0.6"/>
          <stop offset="100%" stop-color="#c8000a" stop-opacity="0"/>
        </radialGradient>
      </defs>
      <ellipse cx="300" cy="205" rx="298" ry="203" fill="url(#figureTone)"/>
    </svg>

    <h1 class="name">Tod Harlick</h1>
    <p class="phone">555.317.0492</p>

    <p class="services">
      <span class="line">Classical Dressage Training</span>
      <span class="line">Modern American Clinics • Lessons • Training Level</span>
      <span class="line level">Prix St. George</span>
    </p>
  </main>
</body>
</html>
```